Chocolate Bar Design

I need packaging design for a new line of chocolate bars.

The new design must fit in with the packaging design for our line of solid chocolate bars. The previous bars are packaged in clear boxes, the new line is in 3x3 kraft boxes so the new design must be visusally appealing, and portray what lies inside as they are not able to view the bar itself.

The new product line is for "Truffle Bars", basically a chocolate bar with a truffle filling. The first three flavors are Ember Tide (Cinnamon and Cayenne, Sea Salt), Cafe Mocha, and Pumpkin Pie.

These are artisan bars, and should reflect in the packaging.

If you view our previous packaging, they are the same design but with a different color for each flavor, which would be ideal.

Industry/Entity Type

Cafe

Requirements
Must have
• Each design should include the front label that has the company name, size of the bar, and name of the bar at minimum. The reverse label must have company name, address, website, and ingredients, at minimum.

Nice to have
• Ideally, I would be able to edit ingredients, and bar names easily.

```html
<!DOCTYPE html>
<html lang="en">
<head>
<meta charset="utf-8">
<title>Marlow Bell Truffle Bar Labels</title>
<link rel="stylesheet" href="https://fonts.googleapis.com/css2?family=Bodoni+Moda:wght@400&family=Arimo&display=swap">
<style>
  :root {
    --paper: #ffffff;
    --card-edge: #d4d4d4;
    --ink-light: #ffffff;
    --ember-core: #be1e2d;
    --ember-ring: #f15a29;
    --mocha-core: #6f4727;
    --mocha-ring: #c2b59b;
    --pumpkin-core: #f7941d;
    --pumpkin-ring: #c49a6c;
  }
  html, body {
    margin: 0;
    padding: 0;
    width: 1200px;
    height: 900px;
    overflow: hidden;
    background: var(--paper);
  }
  .label-sheet {
    position: relative;
    width: 1200px;
    height: 900px;
  }
  .label-card {
    position: absolute;
    width: 325px;
    height: 325px;
    box-sizing: border-box;
    border: 1px solid var(--card-edge);
    background: var(--paper);
  }
  .label-card svg {
    display: block;
  }
  .row-front { top: 103px; }
  .row-back { top: 499px; }
  .col-ember { left: 43px; }
  .col-mocha { left: 436px; }
  .col-pumpkin { left: 827px; }

  .brand-name {
    font-family: "Bodoni Moda", serif;
    font-size: 34px;
    fill: var(--ink-light);
  }
  .brand-tagline {
    font-family: "Bodoni Moda", serif;
    font-size: 9px;
    letter-spacing: 3px;
    fill: var(--ink-light);
  }
  .flavor-name {
    font-family: "Bodoni Moda", serif;
    font-size: 24px;
    fill: var(--ink-light);
  }
  .flavor-note {
    font-family: "Bodoni Moda", serif;
    font-size: 13px;
    fill: var(--ink-light);
  }
  .net-weight {
    font-family: "Bodoni Moda", serif;
    font-size: 8px;
    fill: var(--ink-light);
  }
  .back-brand {
    font-family: "Bodoni Moda", serif;
    font-size: 24px;
    fill: var(--ink-light);
  }
  .back-tagline {
    font-family: "Bodoni Moda", serif;
    font-size: 7px;
    letter-spacing: 2px;
    fill: var(--ink-light);
  }
  .contact-line, .ingredients-line {
    font-family: "Arimo", sans-serif;
    font-size: 14px;
    fill: var(--ink-light);
  }
  .ring-story {
    font-family: "Bodoni Moda", serif;
    font-size: 8px;
    fill: var(--ink-light);
  }
  .core-ember { fill: var(--ember-core); }
  .ring-ember { fill: var(--ember-ring); }
  .core-mocha { fill: var(--mocha-core); }
  .ring-mocha { fill: var(--mocha-ring); }
  .core-pumpkin { fill: var(--pumpkin-core); }
  .ring-pumpkin { fill: var(--pumpkin-ring); }
</style>
</head>
<body>
<main class="label-sheet">

  <!-- Front labels -->
  <section class="label-card row-front col-ember" aria-label="Ember Tide front label">
    <svg width="323" height="323" viewBox="0 0 323 323">
      <circle class="ring-ember" cx="163" cy="161" r="146"/>
      <circle class="core-ember" cx="163" cy="161" r="129"/>
      <text class="brand-name" x="163" y="160" text-anchor="middle">Marlow Bell</text>
      <text class="brand-tagline" x="180" y="174" text-anchor="middle">chocolates</text>
      <text class="flavor-name" x="163" y="220" text-anchor="middle">Ember Tide</text>
      <text class="flavor-note" x="163" y="242" text-anchor="middle">Hand - Crafted</text>
      <text class="net-weight" x="163" y="278" text-anchor="middle">NET WT 3.5oz</text>
    </svg>
  </section>

  <section class="label-card row-front col-mocha" aria-label="Cafe Mocha front label">
    <svg width="323" height="323" viewBox="0 0 323 323">
      <circle class="ring-mocha" cx="163" cy="161" r="146"/>
      <circle class="core-mocha" cx="163" cy="161" r="128"/>
      <text class="brand-name" x="163" y="160" text-anchor="middle">Marlow Bell</text>
      <text class="brand-tagline" x="180" y="174" text-anchor="middle">chocolates</text>
      <text class="flavor-name" x="163" y="220" text-anchor="middle">Cafe Mocha</text>
      <text class="flavor-note" x="163" y="242" text-anchor="middle">Hand - Crafted</text>
      <text class="net-weight" x="163" y="278" text-anchor="middle">NET WT 3.5oz</text>
    </svg>
  </section>

  <section class="label-card row-front col-pumpkin" aria-label="Pumpkin Pie front label">
    <svg width="323" height="323" viewBox="0 0 323 323">
      <circle class="ring-pumpkin" cx="163" cy="161" r="146"/>
      <circle class="core-pumpkin" cx="163" cy="161" r="128"/>
      <text class="brand-name" x="163" y="160" text-anchor="middle">Marlow Bell</text>
      <text class="brand-tagline" x="180" y="174" text-anchor="middle">chocolates</text>
      <text class="flavor-name" x="163" y="220" text-anchor="middle">Pumpkin Pie</text>
      <text class="flavor-note" x="163" y="242" text-anchor="middle">Hand - Crafted</text>
      <text class="net-weight" x="163" y="278" text-anchor="middle">NET WT 3.5oz</text>
    </svg>
  </section>

  <!-- Back labels -->
  <section class="label-card row-back col-ember" aria-label="Ember Tide back label">
    <svg width="323" height="323" viewBox="0 0 323 323">
      <defs>
        <path id="story-path-ember" d="M162,25 A137,137 0 1 1 162,299 A137,137 0 1 1 162,25"/>
      </defs>
      <circle class="core-ember" cx="162" cy="162" r="146"/>
      <text class="ring-story"><textPath href="#story-path-ember" startOffset="2%" textLength="790" lengthAdjust="spacing">Marlow Bell Chocolates is an artisan chocolate confection company based in Alder Bay, WA. We provide a wide range of hand crafted confections to our customers through a select group of retailers, gift shows, and our website.</textPath></text>
      <text class="back-brand" x="162" y="74" text-anchor="middle">Marlow Bell</text>
      <text class="back-tagline" x="175" y="84" text-anchor="middle">chocolates</text>
      <text class="contact-line" x="162" y="162" text-anchor="middle">www.marlowbellchocolates.com</text>
      <text class="contact-line" x="162" y="179" text-anchor="middle">1234 Your Address</text>
      <text class="contact-line" x="162" y="196" text-anchor="middle">Alder Bay, WA</text>
      <text class="ingredients-line" x="162" y="230" text-anchor="middle">Ingredients: Chocolate, Spices</text>
    </svg>
  </section>

  <section class="label-card row-back col-mocha" aria-label="Cafe Mocha back label">
    <svg width="323" height="323" viewBox="0 0 323 323">
      <defs>
        <path id="story-path-mocha" d="M162,25 A137,137 0 1 1 162,299 A137,137 0 1 1 162,25"/>
      </defs>
      <circle class="core-mocha" cx="162" cy="162" r="146"/>
      <text class="ring-story"><textPath href="#story-path-mocha" startOffset="2%" textLength="790" lengthAdjust="spacing">Marlow Bell Chocolates is an artisan chocolate confection company based in Alder Bay, WA. We provide a wide range of hand crafted confections to our customers through a select group of retailers, gift shows, and our website.</textPath></text>
      <text class="back-brand" x="162" y="74" text-anchor="middle">Marlow Bell</text>
      <text class="back-tagline" x="175" y="84" text-anchor="middle">chocolates</text>
      <text class="contact-line" x="162" y="162" text-anchor="middle">www.marlowbellchocolates.com</text>
      <text class="contact-line" x="162" y="179" text-anchor="middle">1234 Your Address</text>
      <text class="contact-line" x="162" y="196" text-anchor="middle">Alder Bay, WA</text>
      <text class="ingredients-line" x="162" y="230" text-anchor="middle">Ingredients: Chocolate, Spices</text>
    </svg>
  </section>

  <section class="label-card row-back col-pumpkin" aria-label="Pumpkin Pie back label">
    <svg width="323" height="323" viewBox="0 0 323 323">
      <defs>
        <path id="story-path-pumpkin" d="M162,25 A137,137 0 1 1 162,299 A137,137 0 1 1 162,25"/>
      </defs>
      <circle class="core-pumpkin" cx="162" cy="162" r="146"/>
      <text class="ring-story"><textPath href="#story-path-pumpkin" startOffset="2%" textLength="790" lengthAdjust="spacing">Marlow Bell Chocolates is an artisan chocolate confection company based in Alder Bay, WA. We provide a wide range of hand crafted confections to our customers through a select group of retailers, gift shows, and our website.</textPath></text>
      <text class="back-brand" x="162" y="74" text-anchor="middle">Marlow Bell</text>
      <text class="back-tagline" x="175" y="84" text-anchor="middle">chocolates</text>
      <text class="contact-line" x="162" y="162" text-anchor="middle">www.marlowbellchocolates.com</text>
      <text class="contact-line" x="162" y="179" text-anchor="middle">1234 Your Address</text>
      <text class="contact-line" x="162" y="196" text-anchor="middle">Alder Bay, WA</text>
      <text class="ingredients-line" x="162" y="230" text-anchor="middle">Ingredients: Chocolate, Spices</text>
    </svg>
  </section>

</main>
</body>
</html>
```